Weather card for guests at Marlow’s Shore Cottage

I am looking to have a card designed for my guests who stay over. The card should show the weather for the next day (emoji's), quote of the day, Activities of the day. It's for a beach house so it should be coastal/Beachy themed. The weather should have a high and a low. (I will fill in each card). It should be front and back. It should be a fun project. Think modern farmhouse. The top of each card should say something like Another great Day at 7 Harbor
Updates

If you google "turn down Service letter" or "hotel weather card". It will provide examples

Target Market(s)

Our guests who visit our beach house

Font styles to use
Sans Serif

Colors
0054AA
0677BA
7BADD7
CADEEF
E8F1F8

Requirements
Must have
• weather options, quote of the day, activity for the day
Nice to have
• Sand, seashells, seagulls
Should not have
• Should not be too busy and not childish

```html
<!DOCTYPE html>
<html lang="en">
<head>
<meta charset="utf-8">
<title>Weather Card · Marlow’s Shore Cottage</title>
<link rel="stylesheet" href="https://fonts.googleapis.com/css2?family=Lexend+Zetta:wght@300&family=Quicksand:wght@500&display=swap">
<style>
  :root {
    --ink: #2e3192;
    --ink-soft: #5a5db0;
    --paper: #f8f6f4;
    --page: #ffffff;
    --edge: #bdbdbd;
    --sand-light: #c9cae6;
  }
  * { box-sizing: border-box; margin: 0; padding: 0; }
  html, body { width: 1200px; height: 1000px; overflow: hidden; background: var(--page); }
  body { position: relative; font-family: "Lexend Zetta", sans-serif; color: var(--ink); }

  .card {
    position: absolute; left: 261px; width: 683px; height: 487px;
    background: var(--paper); border: 1px solid var(--edge);
    box-shadow: 4px 4px 6px rgba(0,0,0,0.18);
  }
  .card--front { top: 8px; }
  .card--back { top: 507px; }

  .label { position: absolute; font-weight: 300; text-transform: uppercase; color: var(--ink-soft); white-space: nowrap; }

  .greeting { left: 29px; top: 40px; font-size: 18px; letter-spacing: -0.5px; }
  .place-name {
    position: absolute; left: 403px; top: 10px; font-family: "Quicksand", sans-serif;
    font-weight: 500; font-size: 66px; color: var(--ink); white-space: nowrap; letter-spacing: -0.5px;
  }

  .rule { position: absolute; left: 29px; border-top: 2px dotted var(--ink-soft); opacity: 0.7; }
  .card--front .rule { top: 87px; width: 626px; }
  .card--back .rule { top: 78px; width: 620px; }

  .section-title { left: 29px; top: 104px; font-size: 17px; }

  .seagulls {
    position: absolute; left: 567px; top: 105px; width: 95px; height: 40px;
    background: radial-gradient(ellipse at center, rgba(46,49,146,0.55), rgba(46,49,146,0) 70%);
  }
  .sand {
    position: absolute;
    background: linear-gradient(90deg, rgba(46,49,146,0.15), rgba(46,49,146,0.4) 30%, rgba(46,49,146,0.25) 60%, rgba(46,49,146,0.15));
    border-radius: 50%;
    filter: blur(3px);
  }
  .card--front .sand { left: 5px; top: 356px; width: 657px; height: 34px; }
  .card--back .sand { left: 20px; top: 436px; width: 642px; height: 28px; }

  .weather-title { left: 29px; top: 404px; font-size: 17px; line-height: 23px; white-space: normal; }
  .temp { top: 456px; font-size: 12px; }
  .temp--high { left: 165px; }
  .temp--low { left: 288px; }
  .divider { position: absolute; left: 248px; top: 404px; height: 63px; border-left: 1px solid var(--ink-soft); opacity: 0.6; }
  .forecast-title { left: 460px; top: 404px; font-size: 17px; }

  .forecast-icons { position: absolute; left: 378px; top: 434px; display: flex; gap: 23px; }
  .forecast-icons svg { width: 38px; height: 38px; fill: none; stroke: var(--ink); stroke-width: 1.3; stroke-linecap: round; stroke-linejoin: round; }

  .activities-title { left: 29px; top: 34px; font-size: 25px; letter-spacing: -0.5px; }
  .seashell {
    position: absolute; left: 577px; top: 20px; width: 82px; height: 48px;
    background: radial-gradient(ellipse at 40% 55%, rgba(46,49,146,0.6), rgba(46,49,146,0.1) 75%);
    border-radius: 45% 55% 50% 50%;
  }
</style>
</head>
<body>

<section class="card card--front">
  <p class="label greeting">Another great day at</p>
  <h1 class="place-name">7 Harbor</h1>
  <div class="rule"></div>

  <h2 class="label section-title">Inspiration</h2>
  <div class="seagulls" role="img" aria-label="Illustration of two seagulls in flight"></div>

  <div class="sand" role="img" aria-label="Scattered sand speckle border"></div>

  <h2 class="label weather-title">Weather<br>Today</h2>
  <span class="label temp temp--high">High</span>
  <div class="divider"></div>
  <span class="label temp temp--low">Low</span>

  <h2 class="label forecast-title">Forecast</h2>
  <div class="forecast-icons">
    <svg viewBox="0 0 38 38" aria-label="Sunny" role="img">
      <circle cx="19" cy="19" r="6"/>
      <path d="M19 5v6M19 27v6M5 19h6M27 19h6M9 9l4 4M25 25l4 4M29 9l-4 4M13 25l-4 4"/>
    </svg>
    <svg viewBox="0 0 38 38" aria-label="Partly cloudy" role="img">
      <circle cx="25" cy="13" r="4.5"/>
      <path d="M25 4v3M32 13h3M30.5 7.5l2-2M19 7.5l-2-2"/>
      <path d="M6 30h24a5 5 0 0 0 0-10 7 7 0 0 0-13-2 6 6 0 0 0-11 6 3 3 0 0 0 0 6z"/>
    </svg>
    <svg viewBox="0 0 38 38" aria-label="Cloudy" role="img">
      <path d="M7 28h23a5 5 0 0 0 0-10 7 7 0 0 0-13-3 6 6 0 0 0-10 5 4 4 0 0 0 0 8z"/>
    </svg>
    <svg viewBox="0 0 38 38" aria-label="Rain" role="img">
      <path d="M7 24h23a5 5 0 0 0 0-10 7 7 0 0 0-13-3 6 6 0 0 0-10 5 4 4 0 0 0 0 8z"/>
      <path d="M12 27v5M17 27v7M22 27v5M27 27v6"/>
    </svg>
    <svg viewBox="0 0 38 38" aria-label="Windy" role="img">
      <path d="M4 14h22a4 4 0 1 0-4-4M4 19h28a4 4 0 1 1-4 4M4 24h16M6 17h18"/>
    </svg>
  </div>
</section>

<section class="card card--back">
  <h2 class="label activities-title">Today’s Activities:</h2>
  <div class="seashell" role="img" aria-label="Engraved-style seashell illustration"></div>
  <div class="rule"></div>
  <div class="sand" role="img" aria-label="Scattered sand speckle border"></div>
</section>

</body>
</html>
```